Modern Spot UV Business Card design

We are a relatively new real estate agency. We need a business card that reflects the professionalism and prestige of our company but is also modern and fresh, based around our logo.
We would love to utilise spot UV.
Happy to let the designers use their imagination and see what they come up with (we're not very creative, so have no ideas for you, sorry) :-)
We'd like one for each staff member, but I've just provided one staff members photo here to avoid confusion.

Target Market(s)

Families

Industry/Entity Type

Real Estate Agent

Contact Information for Business Card

Colin Varga - Director & Principal
Mobile: 0491 527 806
Email: colin.varga@vbrokers.example.com.au
Phone: (08) 7364 9150
Fax: (08) 7364 9182
www.vargabrokersrealestate.example.com.au

Font styles to use
Other font styles liked:
• Kabel Dm BT

Requirements
Must have
• Contact details, logo, photo, spot UV
Nice to have
• Modern interesting features that will make people comment. Nothing too feminine nor too masculine.
Should not have
• No houses! Nothing typical of a real estate agent.

```html
<!DOCTYPE html>
<html lang="en">
<head>
<meta charset="utf-8">
<title>Varga Brokers Real Estate – Business Card</title>
<link href="https://fonts.googleapis.com/css2?family=Ubuntu:wght@400;500&display=swap" rel="stylesheet">
<style>
  :root {
    --page-bg: #ffffff;
    --card-light: #e9e9e9;
    --card-dark: #242424;
    --accent-red: #e03c1f;
    --ink-dark: #2a2a2a;
    --ink-brand: #2b3a5c;
    --ink-light: #ffffff;
  }
  * { margin: 0; padding: 0; box-sizing: border-box; }
  html, body {
    width: 1200px;
    height: 758px;
    overflow: hidden;
    background: var(--page-bg);
    font-family: "Ubuntu", sans-serif;
  }
  .business-card {
    position: absolute;
    left: 250px;
    top: 179px;
    width: 700px;
    height: 400px;
    display: flex;
    flex-direction: column;
    box-shadow: 0 2px 6px rgba(0,0,0,0.18);
  }
  .card-top {
    height: 215px;
    background: var(--card-light);
    display: flex;
    align-items: center;
    padding: 0 52px 0 70px;
    justify-content: space-between;
  }
  .brand {
    display: flex;
    align-items: center;
    gap: 12px;
  }
  .brand-dot {
    width: 30px;
    height: 30px;
    border-radius: 50%;
    background: var(--accent-red);
  }
  .brand-name {
    font-weight: 500;
    font-size: 26px;
    line-height: 1.15;
    color: var(--ink-brand);
  }
  .person {
    text-align: left;
  }
  .person-name {
    font-weight: 400;
    font-size: 46px;
    color: var(--accent-red);
    line-height: 1.05;
  }
  .person-title {
    font-weight: 400;
    font-size: 24px;
    color: var(--ink-dark);
    margin-top: 2px;
  }
  .accent-band {
    height: 14px;
    background: var(--accent-red);
  }
  .card-bottom {
    flex: 1;
    background: var(--card-dark);
    padding: 38px 0 0 58px;
  }
  .contact-list { list-style: none; }
  .contact-item {
    display: flex;
    align-items: center;
    gap: 12px;
    color: var(--ink-light);
    font-size: 21px;
    height: 31px;
  }
  .contact-icon {
    width: 16px;
    height: 16px;
    fill: var(--ink-light);
    flex: none;
  }
</style>
</head>
<body>
  <article class="business-card">
    <header class="card-top">
      <div class="brand">
        <span class="brand-dot"></span>
        <span class="brand-name">Varga Brokers<br>Real Estate</span>
      </div>
      <div class="person">
        <h1 class="person-name">Colin Varga</h1>
        <p class="person-title">Director &amp; Principal</p>
      </div>
    </header>
    <div class="accent-band"></div>
    <section class="card-bottom">
      <ul class="contact-list">
        <li class="contact-item">
          <svg class="contact-icon" viewBox="0 0 16 16"><path d="M4 0h8a1 1 0 0 1 1 1v14a1 1 0 0 1-1 1H4a1 1 0 0 1-1-1V1a1 1 0 0 1 1-1zm1 2v8h6V2zm1 9v1h1v-1zm2 0v1h1v-1zm2 0v1h1v-1zm-4 2v1h1v-1zm2 0v1h1v-1zm2 0v1h1v-1z"/></svg>
          <span>0491 527 806</span>
        </li>
        <li class="contact-item">
          <svg class="contact-icon" viewBox="0 0 16 16"><path d="M3.6 1.2l2.2 2.7-1.4 1.8c.9 2 2.4 3.6 4.4 4.6l1.8-1.4 2.7 2.2-1.2 2.6C7.5 13.6 2.3 8.5 1 3z"/></svg>
          <span>(08) 7364 9150</span>
        </li>
        <li class="contact-item">
          <svg class="contact-icon" viewBox="0 0 16 16"><path d="M1 3h14v1.2L8 8.6 1 4.2zm0 2.6l7 4.4 7-4.4V13H1z"/></svg>
          <span>colin.varga@vbrokers.example.com.au</span>
        </li>
        <li class="contact-item">
          <svg class="contact-icon" viewBox="0 0 16 16"><path d="M8 0a8 8 0 1 0 0 16A8 8 0 0 0 8 0zM4 3.5c1 .3 1.5 1 1.2 2-.4 1 .8 1.5 1.6 1.2 1-.3 1.8.6 1.4 1.6-.5 1.2-1.8 1.4-2 2.8-.1.9-.4 2-1 2.3A6.5 6.5 0 0 1 4 3.5zm7.2 9.7c-.4-1-.1-2 .9-2.7.8-.6 1.8-.3 2.3.4a6.5 6.5 0 0 1-3.2 2.3z"/></svg>
          <span>www.vargabrokersrealestate.example.com.au</span>
        </li>
      </ul>
    </section>
  </article>
</body>
</html>
```